Painting Company Business Card

Brightwell Painting needs a new business card. See attachments for our logo and current card as an example.
We want to utilize the same colors in the logo, and keep all the information that is currently on it. Just need an updated and modern design.
We are open to loosing the Association Logos if it means a better design.
We are also entertaining a spot for a picture of a headshot of the person listed on the card. Head shot can be finished later.

```html
<!DOCTYPE html>
<html lang="en">
<head>
<meta charset="utf-8">
<title>Brightwell Painting – Business Card</title>
<link href="https://fonts.googleapis.com/css2?family=Open+Sans:wght@300;400;600&family=Russo+One&display=swap" rel="stylesheet">
<style>
  :root {
    --olive: #40452f;
    --olive-dark: #353a27;
    --maroon: #6d3b35;
    --paper: #ffffff;
    --logo-grey: #8d8f83;
    --stage: #e8e5e0;
    --ink: #2f3324;
  }
  * { box-sizing: border-box; margin: 0; padding: 0; }
  html, body { width: 1200px; height: 960px; overflow: hidden; }
  body {
    background: var(--stage);
    font-family: "Open Sans", Arial, sans-serif;
    position: relative;
  }
  .card {
    position: absolute;
    left: 250px;
    width: 700px;
    height: 400px;
    box-shadow: 0 8px 24px rgba(0,0,0,0.18);
    overflow: hidden;
  }
  /* Back side */
  .card-back { top: 50px; background: var(--olive); }
  .card-back .brand-name {
    position: absolute;
    left: 48px; top: 70px;
    width: 250px;
    font-family: "Open Sans", Arial, sans-serif;
    font-weight: 600;
    font-size: 40px;
    line-height: 1.05;
    color: var(--logo-grey);
  }
  .services {
    position: absolute;
    left: 330px; top: 120px;
    list-style: none;
  }
  .services li {
    display: flex;
    align-items: center;
    gap: 12px;
    font-family: "Russo One", Arial, sans-serif;
    font-style: italic;
    font-size: 26px;
    letter-spacing: 1px;
    color: var(--paper);
    text-transform: uppercase;
    margin-bottom: 10px;
  }
  .services svg { width: 26px; height: 26px; flex: none; }

  /* Front side */
  .card-front { top: 510px; background: var(--paper); }
  .card-front .brand-name {
    position: absolute;
    left: 48px; top: 140px;
    width: 320px;
    font-family: "Open Sans", Arial, sans-serif;
    font-weight: 600;
    font-size: 44px;
    line-height: 1.05;
    color: var(--olive);
  }
  .headshot-spot {
    position: absolute;
    right: 24px; top: 48px;
    width: 260px; height: 130px;
    background: var(--olive);
  }
  .contact {
    position: absolute;
    right: 24px; top: 196px;
    text-align: right;
    color: var(--ink);
  }
  .contact .person {
    font-weight: 300;
    font-size: 36px;
    line-height: 1;
    text-transform: uppercase;
  }
  .contact .role {
    font-size: 14px;
    font-variant: small-caps;
    letter-spacing: 1px;
    margin: 4px 0 16px;
    text-transform: lowercase;
  }
  .contact .line { font-size: 18px; line-height: 1.35; }
</style>
</head>
<body>
  <section class="card card-back">
    <div class="brand-name">Brightwell Painting</div>
    <ul class="services">
      <li><svg viewBox="0 0 26 26"><rect x="2" y="6" width="17" height="17" fill="none" stroke="#fff" stroke-width="2"/><path d="M6 13 L11 19 L24 3" fill="none" stroke="#fff" stroke-width="2.5"/></svg>Exterior Painting</li>
      <li><svg viewBox="0 0 26 26"><rect x="2" y="6" width="17" height="17" fill="none" stroke="#fff" stroke-width="2"/><path d="M6 13 L11 19 L24 3" fill="none" stroke="#fff" stroke-width="2.5"/></svg>Interior Painting</li>
      <li><svg viewBox="0 0 26 26"><rect x="2" y="6" width="17" height="17" fill="none" stroke="#fff" stroke-width="2"/><path d="M6 13 L11 19 L24 3" fill="none" stroke="#fff" stroke-width="2.5"/></svg>Carpentry</li>
      <li><svg viewBox="0 0 26 26"><rect x="2" y="6" width="17" height="17" fill="none" stroke="#fff" stroke-width="2"/><path d="M6 13 L11 19 L24 3" fill="none" stroke="#fff" stroke-width="2.5"/></svg>Drywall</li>
    </ul>
  </section>

  <section class="card card-front">
    <div class="brand-name">Brightwell Painting</div>
    <div class="headshot-spot" role="img" aria-label="Space for headshot of the card holder"></div>
    <div class="contact">
      <div class="person">Mark Ellison</div>
      <div class="role">Quality Manager</div>
      <div class="line">414-555-0196</div>
      <div class="line">mark.brightwell@mail.com</div>
      <div class="line">brightwellpainting.com</div>
    </div>
  </section>
</body>
</html>
```